Ledgrix Business Card

We need a business card design using the attached logo. The company is a financial services company that provides a dashboard (chart based information) for Executives of small businesses to use to better manage their information. The design must be progressive, make good utilization of the logo and project stability and financial security.

Industry/Entity Type

Financial

```html
<!DOCTYPE html>
<html lang="en">
<head>
<meta charset="utf-8">
<title>Ledgrix Business Card</title>
<link rel="stylesheet" href="https://fonts.googleapis.com/css2?family=Questrial&display=swap">
<style>
  :root {
    --stage: #e9e7e4;
    --card-white: #ffffff;
    --ink: #1b1b1b;
    --brand-red: #a3161d;
    --band-black: #0d0d0d;
    --back-black: #121212;
    --back-black-soft: #1f1f1f;
    --faint: #eeeeee;
  }
  * { box-sizing: border-box; margin: 0; padding: 0; }
  html, body { width: 1200px; height: 784px; overflow: hidden; }
  body {
    background: var(--stage);
    font-family: "Questrial", "Century Gothic", sans-serif;
    color: var(--ink);
    position: relative;
  }
  .card {
    position: absolute;
    top: 238px;
    width: 540px;
    height: 309px;
    border-radius: 4px;
    overflow: hidden;
    box-shadow: 0 8px 24px rgba(0,0,0,0.18);
  }
  .card--front { left: 45px; background: var(--card-white); }
  .card--back {
    left: 615px;
    background: radial-gradient(ellipse at 50% 45%, var(--back-black-soft), var(--back-black) 70%);
    display: flex; align-items: center; justify-content: center;
  }

  .brand {
    position: absolute; left: 34px; top: 40px;
    display: flex; align-items: center; gap: 10px;
  }
  .brand__square { width: 40px; height: 40px; background: var(--ink); border-radius: 4px; }
  .brand__name { font-size: 46px; font-weight: 400; letter-spacing: -0.5px; color: var(--ink); line-height: 1; }

  .brand-mark-faint {
    position: absolute; right: 40px; top: 26px;
    width: 150px; height: 150px; border-radius: 10px;
    background: var(--faint);
  }

  .person { position: absolute; left: 48px; top: 128px; }
  .person__name { font-size: 17px; color: var(--brand-red); letter-spacing: 0.3px; }
  .person__title { font-size: 11px; margin-top: 3px; }

  .contacts { position: absolute; left: 48px; top: 174px; list-style: none; font-size: 14px; line-height: 17px; }
  .contacts li { display: flex; align-items: flex-start; gap: 7px; }
  .contacts svg { width: 14px; height: 14px; flex: none; margin-top: 2px; fill: var(--brand-red); }
  .contacts .no-icon { padding-left: 21px; }

  .footer-band { position: absolute; left: 0; bottom: 0; width: 540px; height: 80px; }

  .web-address {
    color: var(--brand-red);
    font-size: 17px;
    letter-spacing: 6px;
  }
</style>
</head>
<body>

<section class="card card--front" aria-label="Business card front">
  <div class="brand">
    <span class="brand__square"></span>
    <span class="brand__name">Ledgrix</span>
  </div>
  <div class="brand-mark-faint"></div>

  <div class="person">
    <p class="person__name">Dana Whitfield</p>
    <p class="person__title">Manager</p>
  </div>

  <svg class="footer-band" viewBox="0 0 540 80" preserveAspectRatio="none" aria-hidden="true">
    <polygon points="0,58 540,18 540,26 0,66" fill="var(--brand-red)"/>
    <polygon points="0,66 540,26 540,80 0,80" fill="var(--band-black)"/>
  </svg>

  <ul class="contacts">
    <li>
      <svg viewBox="0 0 16 16"><path d="M3 1l3 3-1.5 2a9 9 0 005 5L11.5 9.5l3 3-2 2.5C6 15 1 10 1 3z"/></svg>
      <span>555-318-4420</span>
    </li>
    <li>
      <svg viewBox="0 0 16 16"><rect x="4" y="1" width="8" height="14" rx="1.5"/><rect x="5.5" y="3" width="5" height="8" fill="#fff"/></svg>
      <span>555-318-4421</span>
    </li>
    <li>
      <svg viewBox="0 0 16 16"><path d="M8 1l7 6.5h-2V15H9.5v-4h-3v4H3V7.5H1z"/></svg>
      <span>4180 Marlow Ave</span>
    </li>
    <li class="no-icon"><span>Denton, TX 76201</span></li>
    <li>
      <svg viewBox="0 0 16 16"><rect x="1" y="3" width="14" height="10" rx="1"/><path d="M1.5 4l6.5 5 6.5-5" fill="none" stroke="#fff" stroke-width="1.2"/></svg>
      <span>d.whitfield@ledgrixadvisory.com</span>
    </li>
  </ul>
</section>

<section class="card card--back" aria-label="Business card back">
  <p class="web-address">www.ledgrixadvisory.com</p>
</section>

</body>
</html>
```